RTV CRAFTED

building services
decks
pergola
renovation
extensions
general building

Target Market(s)

middle to upper class

Industry/Entity Type

building

Contact Information for Business Card

my details 0427839152 pkharlow47@mailvane.net BLD574926

Font styles to use
Serif

Colors
00AB8E
00BBA5
67D7C9
C6EFE9
E9F9F6

Requirements
Must have
• logo on the front and details on the back
Nice to have
• sharp and clean lines

```html
<!DOCTYPE html>
<html lang="en">
<head>
<meta charset="utf-8">
<title>RTV Crafted – Business Cards</title>
<link rel="stylesheet" href="https://fonts.googleapis.com/css2?family=Libre+Caslon+Text:wght@400&family=Jost:wght@400&display=swap">
<style>
  :root {
    --teal: #14ae91;
    --ink: #111111;
    --paper: #ffffff;
    --backdrop: #e4e5e7;
    --serif: "Libre Caslon Text", "Times New Roman", serif;
    --sans: "Jost", "Futura", sans-serif;
  }
  * { box-sizing: border-box; margin: 0; padding: 0; }
  html, body { width: 1200px; height: 1200px; overflow: hidden; }
  body { background: var(--backdrop); position: relative; font-family: var(--serif); }

  .card {
    position: absolute;
    top: 457px;
    width: 420px;
    height: 240px;
  }
  .card--details { left: 153px; background: var(--paper); }
  .card--brand { left: 624px; background: var(--teal); display: flex; align-items: center; justify-content: center; }

  .wordmark {
    font-family: var(--serif);
    font-weight: 400;
    letter-spacing: 0.06em;
    white-space: nowrap;
  }
  .card--details .wordmark {
    position: absolute;
    left: 17px;
    top: 38px;
    font-size: 20px;
    color: var(--teal);
  }
  .card--brand .wordmark {
    font-size: 38px;
    color: var(--paper);
  }

  .services {
    position: absolute;
    right: 16px;
    top: 19px;
    list-style: none;
    text-align: right;
  }
  .services li {
    font-family: var(--serif);
    font-size: 10.5px;
    line-height: 14.3px;
    color: var(--ink);
    letter-spacing: 0.01em;
    display: flex;
    justify-content: flex-end;
    align-items: center;
    gap: 8px;
  }
  .services li::after {
    content: "";
    width: 7px;
    height: 7px;
    border-radius: 50%;
    background: var(--teal);
  }

  .divider {
    position: absolute;
    left: 15px;
    right: 16px;
    top: 136px;
    border-top: 1px solid var(--ink);
  }

  .contact {
    position: absolute;
    right: 17px;
    top: 164px;
    text-align: right;
    font-family: var(--sans);
    color: var(--ink);
  }
  .contact__phone, .contact__email { font-size: 11.5px; line-height: 15px; }
  .contact__licence { font-size: 16px; line-height: 22px; margin-top: 1px; }
</style>
</head>
<body>
  <section class="card card--details" aria-label="Business card, details side">
    <p class="wordmark">RTV CRAFTED</p>
    <ul class="services">
      <li>BUILDING SERVICES</li>
      <li>DECKS</li>
      <li>PERGOLA</li>
      <li>RENOVATION</li>
      <li>EXTENSIONS</li>
      <li>GENERAL BUILDING</li>
    </ul>
    <div class="divider"></div>
    <div class="contact">
      <p class="contact__phone">042 783 9152</p>
      <p class="contact__email">pkharlow47@mailvane.net</p>
      <p class="contact__licence">BLD574926</p>
    </div>
  </section>

  <section class="card card--brand" aria-label="Business card, brand side">
    <p class="wordmark">RTV CRAFTED</p>
  </section>
</body>
</html>
```